Modern Business Cards and Stationary for a Dentist
Derek M. Thalby, DDS, PLLC
Modern Business Cards and Stationary for a Dentist - Health
Creative Brief
Professional
Derek M. Thalby, DDS and Joanne R. Thalby, DDS
General Dentistry
318 West Brannig Street Larkwood, TX 78539
thalbydds@mailvesta.com
I need business cards and letterhead. There are two doctors in the office, please put both names on the business cards. They do not need separate cards. Please put the phone number for After Hours underneath the fax number. That number is 830-555-4172. I would like the front of the card to be colorful. But I would like the back of the card to be predominately white with color accents so that it is easy to read once the appointment information is written on it. Please try to incorporate the logo on the back as well.
Appointment card on the back. Line for the name. Under the line "Has an appointment on" then checkboxes for days of the week M,T,W,Th,F. Then another line for the Date and Time of the appointment and another line for Notes. Underneath everything the sentence: If you are unable to keep this appointment, please notify us within 24 hours.

```html
<!DOCTYPE html>
<html lang="en">
<head>
<meta charset="utf-8">
<title>Derek M. Thalby, DDS, PLLC — Stationery</title>
<link rel="stylesheet" href="https://fonts.googleapis.com/css2?family=Montserrat:wght@400;500;600;700&display=swap">
<style>
  :root {
    --maroon: #7a1c3a;
    --maroon-deep: #5e1129;
    --paper: #ffffff;
    --ink: #4a4146;
    --soft: #9a8f94;
    --backdrop: #2c2b2d;
    --faint: #f1e9ec;
  }
  * { box-sizing: border-box; margin: 0; padding: 0; }
  html, body { width: 1200px; height: 754px; overflow: hidden; }
  body {
    background: var(--backdrop);
    font-family: "Montserrat", sans-serif;
    color: var(--ink);
    position: relative;
  }
  .sheet {
    position: absolute;
    background: var(--paper);
    overflow: hidden;
    box-shadow: 0 4px 14px rgba(0,0,0,.35);
  }
  .edge-band { position: absolute; left: 0; top: 0; height: 100%; }
  .practice-name {
    position: absolute;
    display: flex; align-items: center; gap: 6px;
    font-weight: 600; color: var(--maroon);
    letter-spacing: .04em; text-transform: uppercase;
    white-space: nowrap;
  }
  .practice-name .mark-square {
    width: 12px; height: 12px; background: var(--maroon); flex: none;
  }
  .contact-block {
    position: absolute; font-size: 7px; line-height: 1.6; color: var(--soft);
  }
  .faint-circle {
    position: absolute; border-radius: 50%; background: var(--faint);
  }

  /* Letterhead */
  .letterhead { left: 40px; top: 40px; width: 520px; height: 674px; }
  .letterhead .practice-name { left: 64px; top: 36px; font-size: 14px; }
  .letterhead .practice-name .mark-square { width: 16px; height: 16px; }
  .letterhead .contact-block { right: 34px; top: 34px; text-align: right; font-size: 8px; }
  .letterhead .faint-circle { width: 200px; height: 200px; left: 185px; top: 240px; }

  /* Envelope front */
  .envelope-front { left: 600px; top: 40px; width: 400px; height: 184px; }
  .envelope-front .practice-name { left: 40px; top: 20px; font-size: 9px; }
  .envelope-front .contact-block { left: 58px; top: 38px; }
  .envelope-front .faint-circle { width: 100px; height: 100px; left: 70px; top: 72px; }

  /* Envelope back */
  .envelope-back { left: 600px; top: 262px; width: 400px; height: 184px; }
  .envelope-back .flap { position: absolute; inset: 0; }
  .envelope-back .practice-name { left: 50%; top: 64px; transform: translateX(-50%); font-size: 9px; }

  /* Business cards */
  .card { width: 280px; height: 160px; top: 500px; }
  .card-back { left: 600px; }
  .card-front { left: 880px; background: var(--maroon); color: #fff; }

  .card-back .practice-name { left: 18px; top: 12px; font-size: 8px; }
  .card-back .practice-name .mark-square { width: 9px; height: 9px; }
  .appointment-form {
    position: absolute; left: 18px; right: 16px; top: 30px;
    font-size: 7.5px; color: var(--ink);
  }
  .form-title {
    font-weight: 700; color: var(--maroon); text-transform: uppercase;
    letter-spacing: .08em; font-size: 8px; margin-bottom: 6px;
  }
  .form-line { display: flex; align-items: flex-end; gap: 4px; margin-bottom: 6px; }
  .form-line .fill { flex: 1; border-bottom: 1px solid var(--soft); height: 8px; }
  .weekday-row { display: flex; gap: 10px; margin: 3px 0 7px; }
  .weekday { display: flex; align-items: center; gap: 3px; }
  .weekday .box { width: 8px; height: 8px; border: 1px solid var(--maroon); }
  .notice { font-size: 6px; color: var(--soft); margin-top: 2px; }
  .card-back .phone-strip {
    position: absolute; left: 0; bottom: 0; width: 100%; height: 16px;
    background: var(--maroon); color: #fff; font-size: 7.5px; font-weight: 600;
    display: flex; align-items: center; padding-left: 18px; letter-spacing: .04em;
  }

  .card-front .practice-name { left: 20px; top: 18px; font-size: 9px; color: #fff; }
  .card-front .practice-name .mark-square { background: #fff; width: 10px; height: 10px; }
  .doctor-names { position: absolute; left: 20px; top: 44px; font-size: 8.5px; font-weight: 600; line-height: 1.5; }
  .doctor-names .specialty { font-weight: 400; font-size: 7px; opacity: .8; }
  .card-front .contact-block { left: 20px; bottom: 14px; right: 30px; color: #fff; opacity: .92; font-size: 7px; }
  .card-front .white-swoosh { position: absolute; right: 0; top: 0; height: 100%; }
</style>
</head>
<body>

<section class="sheet letterhead" aria-label="Letterhead">
  <svg class="edge-band" width="60" height="674" viewBox="0 0 60 674" preserveAspectRatio="none">
    <path d="M0 0 H50 C28 80 22 200 20 674 H0 Z" fill="var(--maroon)"/>
  </svg>
  <div class="practice-name"><span class="mark-square"></span>Derek M. Thalby, DDS, PLLC</div>
  <div class="contact-block">
    318 West Brannig Street<br>Larkwood, TX 78539<br>Phone (830) 555-0193<br>After Hours 830-555-4172<br>thalbydds@mailvesta.com
  </div>
  <div class="faint-circle"></div>
</section>

<section class="sheet envelope-front" aria-label="Envelope front">
  <svg class="edge-band" width="30" height="184" viewBox="0 0 30 184" preserveAspectRatio="none">
    <path d="M0 0 H26 C16 40 12 100 12 184 H0 Z" fill="var(--maroon)"/>
  </svg>
  <div class="practice-name"><span class="mark-square"></span>Derek M. Thalby, DDS, PLLC</div>
  <div class="contact-block">318 West Brannig Street<br>Larkwood, TX 78539</div>
  <div class="faint-circle"></div>
</section>

<section class="sheet envelope-back" aria-label="Envelope back">
  <svg class="flap" width="400" height="184" viewBox="0 0 400 184">
    <path d="M0 0 L200 100 L400 0" fill="none" stroke="#d9d3d6" stroke-width="1"/>
  </svg>
  <div class="practice-name"><span class="mark-square"></span>Derek M. Thalby, DDS, PLLC</div>
</section>

<section class="sheet card card-back" aria-label="Appointment card">
  <div class="practice-name"><span class="mark-square"></span>Derek M. Thalby, DDS, PLLC</div>
  <div class="appointment-form">
    <div class="form-title">Next Appointment</div>
    <div class="form-line"><span>Name</span><span class="fill"></span></div>
    <div>Has an appointment on</div>
    <div class="weekday-row">
      <span class="weekday"><span class="box"></span>M</span>
      <span class="weekday"><span class="box"></span>T</span>
      <span class="weekday"><span class="box"></span>W</span>
      <span class="weekday"><span class="box"></span>Th</span>
      <span class="weekday"><span class="box"></span>F</span>
    </div>
    <div class="form-line"><span>Date &amp; Time</span><span class="fill"></span></div>
    <div class="form-line"><span>Notes</span><span class="fill"></span></div>
    <p class="notice">If you are unable to keep this appointment, please notify us within 24 hours.</p>
  </div>
  <div class="phone-strip">(830) 555-0193</div>
</section>

<section class="sheet card card-front" aria-label="Business card front">
  <svg class="white-swoosh" width="40" height="160" viewBox="0 0 40 160" preserveAspectRatio="none">
    <path d="M40 0 H30 C20 50 24 110 36 160 H40 Z" fill="#fff" opacity=".9"/>
  </svg>
  <div class="practice-name"><span class="mark-square"></span>Derek M. Thalby, DDS, PLLC</div>
  <div class="doctor-names">
    Derek M. Thalby, DDS<br>Joanne R. Thalby, DDS<br><span class="specialty">General Dentistry</span>
  </div>
  <div class="contact-block">
    318 West Brannig Street, Larkwood, TX 78539<br>
    Phone (830) 555-0193 · Fax (830) 555-0194<br>
    After Hours 830-555-4172<br>
    thalbydds@mailvesta.com
  </div>
</section>

</body>
</html>
```